Travel Blogger Business Card for roamquill.net

I need a two-sided business card for a travel blogging website. The card should be both professional and fun at the same time. This is for the website www.roamquill.net

I don't necessarily think that the current logo on the website needs to be used on the business card but it can be. I am very flexible with ideas

Target Market(s)

Travel agencies that will be met at a conference.

Industry/Entity Type

Travel

Contact Information for Business Card

Company Name: Roam Quill.net
Name: Bertrand Olesky
Voice: +1-(345)-402-7731
Address: Coral Reach Shore, Grand Cayman, Cayman Islands
Email: ceo@roamquill.net

Colors
0592cd
0355a3
3176b5
33a6d7
85cae6
85acd3

Requirements
Must have
• Website address and name should be bigger than address, phone number, and email.

```html
<!DOCTYPE html>
<html lang="en">
<head>
<meta charset="utf-8">
<title>Roam Quill – Business Card</title>
<link rel="stylesheet" href="https://fonts.googleapis.com/css2?family=Arimo:wght@400;700&family=Open+Sans:wght@400&family=Saira+Semi+Condensed:wght@600&family=Tinos&display=swap">
<style>
  :root {
    --stage: #e4e4e4;
    --paper: #ffffff;
    --ink-grey: #8c8c8c;
    --ink-soft: #9a9a9a;
    --rule: #c6c6c6;
    --stripe-deep: #0b56a6;
    --stripe-mid: #2a76b6;
    --stripe-core: #1992cf;
    --stripe-sky: #2fa5d8;
    --stripe-pale: #85c9e9;
    --frame: rgba(255, 255, 255, 0.55);
    --white: #ffffff;
  }
  * { margin: 0; padding: 0; box-sizing: border-box; }
  html, body {
    width: 1200px; height: 1000px; overflow: hidden;
    background: var(--stage);
  }
  .canvas { position: relative; width: 1200px; height: 1000px; }

  .card { position: absolute; width: 642px; height: 385px; overflow: hidden; }

  /* Back side */
  .card--back { left: 456px; top: 76px; background: var(--paper); }
  .holder {
    position: absolute; right: 86px; top: 110px; text-align: right;
    color: var(--ink-grey);
  }
  .holder__name {
    font-family: "Arimo", Arial, sans-serif; font-size: 22px; line-height: 1;
  }
  .holder__name strong { font-weight: 700; }
  .holder__role {
    margin-top: 6px; font-family: "Arimo", Arial, sans-serif; font-size: 16px; line-height: 1;
  }
  .holder__company { font-family: "Tinos", "Times New Roman", serif; font-size: 14px; }
  .divider {
    position: absolute; left: 0; right: 0; top: 177px; height: 2px; background: var(--rule);
  }
  .contacts {
    position: absolute; left: 107px; top: 214px; list-style: none;
    font-family: "Open Sans", Arial, sans-serif; font-size: 16.5px; color: var(--ink-soft);
  }
  .contacts li { display: flex; align-items: center; height: 31px; }
  .contacts svg { width: 16px; height: 16px; margin-right: 16px; fill: none; stroke: var(--ink-soft); stroke-width: 1.6; }
  .contacts svg.solid { fill: var(--ink-soft); stroke: none; }

  /* Front side */
  .card--front { left: 137px; top: 506px; }
  .card__stripes { position: absolute; inset: 0; }
  .frame {
    position: absolute; left: 42px; top: 42px; width: 558px; height: 303px;
    border: 3px solid var(--frame);
  }
  .brand {
    position: absolute; left: 96px; top: 180px;
    font-family: "Saira Semi Condensed", Arial, sans-serif; font-weight: 600;
    font-size: 52px; line-height: 1; color: var(--white); letter-spacing: 0.5px;
  }
</style>
</head>
<body>
<main class="canvas">

  <section class="card card--back" aria-label="Card back">
    <div class="holder">
      <p class="holder__name">Bertrand <strong>Olesky</strong></p>
      <p class="holder__role">CEO <span class="holder__company">Roam Quill</span></p>
    </div>
    <div class="divider"></div>
    <ul class="contacts">
      <li>
        <svg viewBox="0 0 16 16"><circle cx="8" cy="8" r="6.8"/><path d="M5.6 4.6l1.3 1.5-.8 1a5 5 0 0 0 2.8 2.8l1-.8 1.5 1.3-.9 1.1c-2.6-.3-5.1-2.8-5.4-5.4z" fill="var(--ink-soft)" stroke="none"/></svg>
        <span>+1-(345)-402-7731</span>
      </li>
      <li>
        <svg class="solid" viewBox="0 0 16 16"><path d="M1 4h14v9H1z"/><path d="M1.5 4.5L8 9l6.5-4.5" stroke="#fff" stroke-width="1.2" fill="none"/></svg>
        <span>ceo@roamquill.net</span>
      </li>
      <li>
        <svg viewBox="0 0 16 16"><circle cx="8" cy="8" r="6.5"/><ellipse cx="8" cy="8" rx="2.8" ry="6.5"/><path d="M1.5 8h13M2.5 5h11M2.5 11h11"/></svg>
        <span>www.roamquill.net</span>
      </li>
      <li>
        <svg class="solid" viewBox="0 0 16 16"><path d="M8 1a4.5 4.5 0 0 0-4.5 4.5C3.5 9 8 15 8 15s4.5-6 4.5-9.5A4.5 4.5 0 0 0 8 1zm0 6.3a1.8 1.8 0 1 1 0-3.6 1.8 1.8 0 0 1 0 3.6z"/></svg>
        <span>Coral Reach Shore, Grand Cayman, Cayman Islands</span>
      </li>
    </ul>
  </section>

  <section class="card card--front" aria-label="Card front">
    <svg class="card__stripes" viewBox="0 0 642 385" width="642" height="385" aria-hidden="true">
      <rect width="642" height="385" fill="var(--stripe-deep)"/>
      <polygon points="-187,0 642,0 642,829 198,385 0,385 0,187" fill="var(--stripe-mid)"/>
      <polygon points="28,0 642,0 642,614 413,385" fill="var(--stripe-core)"/>
      <polygon points="243,0 642,0 642,399 628,385" fill="var(--stripe-sky)"/>
      <polygon points="453,0 642,0 642,189" fill="var(--stripe-pale)"/>
    </svg>
    <div class="frame"></div>
    <p class="brand">ROAM QUILL</p>
  </section>

</main>
</body>
</html>
```